Harlow Grading and Septic needs a flyer to submit to contractors to offer our services

I need a sleek profession one page full color high gloss document showcasing our services to give to Mobile Home Companies and contractors that need our services.

Home Builders. Mobile Home Salesmen. People Building new homes.

Construction

Serif
Sans Serif

• Phone Number. Email address. Logo. Services offered: Mobile Home Pads, Meter Pole Placement and Connection, Waterline Connection, On Site Septic System Installs
• Jokes, Nothing trying to be cute

```html
<!DOCTYPE html>
<html lang="en">
<head>
<meta charset="utf-8">
<title>Harlow Grading and Septic – Services Flyer</title>
<link rel="stylesheet" href="https://fonts.googleapis.com/css2?family=Montserrat:wght@400;500;700;800&family=Oswald:wght@400;500&display=swap">
<style>
  :root {
    --page-bg: #e6e6e6;
    --paper: #ffffff;
    --navy-dark: #22304a;
    --navy: #1c3a60;
    --blue: #12508a;
    --blue-text: #17508a;
    --foliage: #5f7a4a;
    --sky: #a9c4da;
    --soil-light: #d2ab80;
    --soil: #b0825a;
    --soil-deep: #8f6542;
    --concrete: #dcd6cb;
    --lid-green: #2f7d5c;
    --siding: #c9ccd0;
    --map-paper: #ece6d6;
    --map-edge: #c7bfa8;
    --map-water: #b9cdd6;
    --map-road: #d9b9a8;
  }
  * { box-sizing: border-box; margin: 0; padding: 0; }
  html, body { width: 1200px; height: 1200px; overflow: hidden; }
  body { background: var(--page-bg); position: relative; font-family: "Montserrat", Arial, sans-serif; }

  .flyer {
    position: absolute; left: 291px; top: 68px;
    width: 618px; height: 1063px;
    background: var(--paper); overflow: hidden;
    box-shadow: 0 8px 30px rgba(0,0,0,.12);
  }

  .photo { position: absolute; top: 24px; width: 276px; height: 439px; }
  .photo--tank {
    left: 20px;
    background:
      radial-gradient(ellipse 38% 30% at 30% 88%, rgba(47,125,92,.55), transparent 70%),
      radial-gradient(ellipse 30% 22% at 65% 76%, rgba(47,125,92,.45), transparent 70%),
      radial-gradient(ellipse 30% 35% at 25% 25%, rgba(206,170,60,.55), transparent 70%),
      linear-gradient(180deg, var(--sky) 0%, var(--foliage) 18%, var(--soil-light) 40%, var(--soil) 58%, var(--concrete) 78%, #e9e4da 100%);
  }
  .photo--trench {
    left: 322px;
    background:
      radial-gradient(ellipse 35% 22% at 85% 22%, rgba(220,223,228,.9), transparent 70%),
      radial-gradient(ellipse 22% 14% at 48% 30%, rgba(40,40,40,.55), transparent 70%),
      radial-gradient(ellipse 28% 45% at 50% 68%, rgba(143,101,66,.65), transparent 75%),
      linear-gradient(180deg, var(--foliage) 0%, #8c9a72 12%, var(--soil-light) 32%, var(--soil) 60%, var(--soil-deep) 85%, var(--soil) 100%);
  }

  .brand-cap {
    position: absolute; left: 135px; top: -148px;
    width: 348px; height: 348px; border-radius: 50%;
    background: var(--paper);
  }
  .brand {
    position: absolute; left: 0; right: 0; top: 190px;
    text-align: center; color: var(--navy);
    font-weight: 800; line-height: 1.05;
  }
  .brand__name { font-size: 40px; letter-spacing: 3px; }
  .brand__sub { font-size: 15px; letter-spacing: 1px; margin-top: 6px; }
  .brand__phone { font-size: 15px; letter-spacing: 2px; margin-top: 8px; }

  .services-band {
    position: absolute; left: 0; top: 463px; width: 618px; height: 377px;
    background: linear-gradient(90deg, var(--navy-dark) 0%, var(--navy-dark) 35%, var(--blue) 100%);
  }
  .pill {
    position: absolute; left: 153px; top: 28px; width: 311px; height: 56px;
    border: 2px solid #fff; border-radius: 28px;
    color: #fff; font-size: 25px; font-weight: 500; letter-spacing: 1px;
    display: flex; align-items: center; justify-content: center;
  }
  .service {
    position: absolute; top: 104px; width: 100px; height: 100px; border-radius: 50%;
    background: #fff; color: var(--blue-text);
    font-family: "Oswald", "Arial Narrow", sans-serif; font-size: 14.5px; line-height: 16px;
    text-transform: uppercase; text-align: center;
    display: flex; align-items: center; justify-content: center;
  }
  .area-title {
    position: absolute; left: 0; right: 0; top: 240px;
    text-align: center; color: #fff; font-size: 25px; font-weight: 500; letter-spacing: 1px;
  }

  .map-ring {
    position: absolute; left: 195px; top: 739px; width: 228px; height: 228px;
    border-radius: 50%; background: var(--paper);
  }
  .map {
    position: absolute; left: 13px; top: 13px; width: 202px; height: 202px; border-radius: 50%;
    background:
      radial-gradient(circle at 45% 50%, rgba(250,248,242,.95) 0%, rgba(250,248,242,0) 35%),
      radial-gradient(ellipse 40% 30% at 85% 40%, rgba(217,185,168,.7), transparent 70%),
      radial-gradient(ellipse 30% 40% at 10% 75%, rgba(185,205,214,.8), transparent 70%),
      radial-gradient(ellipse 30% 25% at 80% 85%, rgba(185,205,214,.6), transparent 70%),
      radial-gradient(circle at 50% 50%, var(--map-paper) 55%, var(--map-edge) 100%);
  }

  .contact {
    position: absolute; top: 1001px; height: 28px;
    display: flex; align-items: center; gap: 10px;
    color: var(--blue-text); font-size: 17px; font-weight: 500; letter-spacing: .5px;
  }
  .contact--phone { left: 20px; }
  .contact--email { left: 217px; }
  .contact svg { width: 28px; height: 28px; flex: none; }
</style>
</head>
<body>
  <main class="flyer">
    <div class="photo photo--tank" role="img" aria-label="Photo: excavator beside a freshly installed concrete septic tank with green lids"></div>
    <div class="photo photo--trench" role="img" aria-label="Photo: worker inspecting a deep excavated trench beside a mobile home"></div>

    <div class="brand-cap">
      <div class="brand">
        <div class="brand__name">HARLOW</div>
        <div class="brand__sub">GRADING AND SEPTIC</div>
        <div class="brand__phone">555.214.0187</div>
      </div>
    </div>

    <section class="services-band">
      <div class="pill">SERVICES INCLUDE</div>
      <div class="service" style="left:21px">Mobile<br>Home<br>Pads</div>
      <div class="service" style="left:140px">Meter Pole<br>and<br>Electric</div>
      <div class="service" style="left:259px">Water<br>Lines<br>Connection</div>
      <div class="service" style="left:377px">Septic<br>Systems<br>Installs</div>
      <div class="service" style="left:495px">Septic<br>Design and Site<br>Evaluation</div>
      <h2 class="area-title">SERVICES AREA</h2>
    </section>

    <div class="map-ring">
      <div class="map" role="img" aria-label="Road map of the service area in north and east Texas"></div>
    </div>

    <div class="contact contact--phone">
      <svg viewBox="0 0 28 28" aria-hidden="true"><circle cx="14" cy="14" r="14" fill="#17508a"/><path d="M10.2 7.5c.5-.3 1.1-.1 1.4.4l1.3 2.4c.3.5.1 1.1-.3 1.4l-1 .7c.7 1.6 1.9 2.9 3.5 3.7l.8-1c.4-.4 1-.5 1.4-.2l2.3 1.5c.5.3.6 1 .3 1.4l-1 1.4c-.5.7-1.4 1-2.2.7-4-1.5-6.9-4.6-8.2-8.6-.2-.8.1-1.7.8-2.1z" fill="#fff"/></svg>
      <span>555 214 0187</span>
    </div>
    <div class="contact contact--email">
      <svg viewBox="0 0 28 28" aria-hidden="true"><circle cx="14" cy="14" r="14" fill="#17508a"/><rect x="7.5" y="9.5" width="13" height="9" fill="none" stroke="#fff" stroke-width="1.4"/><path d="M7.5 9.5l6.5 5 6.5-5" fill="none" stroke="#fff" stroke-width="1.4"/></svg>
      <span>owen@harlowgradingandseptic.com</span>
    </div>
  </main>
</body>
</html>
```